Advanced training flyer for defence industry - professional

U.S. Export Controls are some of the most complex and stringent in the world. The U.S. Government regulates the transfer of U.S. origin goods and technical data throughout the world, with the intent of preventing unauthorised transfer of technology and know-how.

These controls extend world-wide and can impact anyone dealing in U.S. controlled goods or technology.

This three-day advanced course is designed to give attendees a greater understanding of U.S. Export Controls from a non-U.S. perspective in practical and relevant terms. Though we will cover a lot of material the course is designed for practitioner with an existing knowledge.

We need a flyer design for an advanced course for the previously mentioned content.

Please include text boxes in order for the form to be completed online.

defence industry

Training

• Please include text boxes so that the form can be completed online.
• flags incorporated

```html
<!DOCTYPE html>
<html lang="en">
<head>
<meta charset="utf-8">
<title>Advanced Defence – EAR &amp; ITAR Training</title>
<link rel="stylesheet" href="https://fonts.googleapis.com/css2?family=Lato:wght@400;700&family=Roboto+Condensed:wght@400;700&display=swap">
<style>
:root{
  --green:#2f7d13;
  --green-dark:#24640d;
  --cyan:#3fc9ea;
  --cyan-light:#8fe2f6;
  --white:#ffffff;
  --ink:#1d1d1d;
  --stage:#e6e6e6;
}
*{box-sizing:border-box;margin:0;padding:0}
html,body{width:1200px;height:899px;overflow:hidden;background:var(--stage)}
.brochure{position:absolute;left:20px;top:36px;width:1160px;height:826px;overflow:hidden;background:var(--white);font-family:"Lato",sans-serif}
.backdrop{position:absolute;inset:0}
.panel-left,.panel-right{position:absolute;top:0;height:100%}
.panel-left{left:0;width:577px}
.panel-right{left:577px;width:583px}
.tab{position:absolute;left:0;height:26px;padding:0 40px 0 16px;display:flex;align-items:center;font-family:"Roboto Condensed",sans-serif;font-weight:700;font-size:15px;letter-spacing:.5px;text-transform:uppercase;clip-path:polygon(0 0,88% 0,100% 100%,0 100%)}
.tab--light{background:var(--white);color:var(--green-dark)}
.tab--cyan{background:var(--cyan);color:var(--white)}
.copy{position:absolute;left:16px;width:540px;font-size:12.5px;line-height:1.4}
.copy--dark{color:var(--ink)}
.copy--light{color:var(--white)}
.discounts{position:absolute;left:16px;list-style:none;font-size:12.5px;font-weight:700;color:var(--ink)}
.discounts li{margin-bottom:9px;padding-left:14px;position:relative}
.discounts li::before{content:"";position:absolute;left:0;top:5px;width:6px;height:6px;border-radius:50%;background:var(--white)}
.venues{position:absolute;left:30px;top:598px;display:flex;gap:30px;font-size:12.5px;color:var(--ink);line-height:1.3;list-style:none}
.venues li{padding-left:12px;position:relative}
.venues li::before{content:"";position:absolute;left:0;top:6px;width:4px;height:4px;background:var(--green)}
.contact{position:absolute;left:0;width:577px;top:724px;text-align:center;color:var(--white)}
.contact h3{font-family:"Lato",sans-serif;font-weight:700;font-size:15px;color:var(--cyan-light);text-decoration:underline;margin-bottom:12px}
.contact p{font-weight:700;font-size:15.5px;line-height:1.45}
.brand-seal{position:absolute;left:334px;top:137px;width:164px;height:164px;border-radius:50%;background:var(--white);display:flex;align-items:center;justify-content:center;text-align:center}
.brand-name{font-family:"Roboto Condensed",sans-serif;font-weight:700;color:var(--green);text-transform:uppercase;line-height:1.05}
.brand-seal .brand-name{font-size:19px}
.brand-lockup{position:absolute;left:40px;top:478px;display:flex;align-items:center;gap:14px}
.brand-dot{width:82px;height:82px;border-radius:50%;background:var(--cyan)}
.brand-lockup .brand-name{font-size:30px}
.course-title{position:absolute;left:37px;top:604px;font-family:"Roboto Condensed",sans-serif;font-weight:700;font-size:44px;color:var(--green-dark);letter-spacing:.3px}
.course-subtitle{position:absolute;left:33px;top:655px;width:367px;height:36px;background:var(--cyan);color:var(--white);font-family:"Roboto Condensed",sans-serif;font-size:24px;letter-spacing:5px;display:flex;align-items:center;justify-content:center}
.course-dates{position:absolute;left:33px;top:699px;width:367px;height:96px;background:var(--green-dark);color:var(--white);font-family:"Roboto Condensed",sans-serif}
.course-dates h2{font-size:29px;font-weight:700;text-align:center;margin-top:4px}
.course-dates ul{list-style:none;margin:6px 0 0 18px;font-size:14px;font-weight:700}
.course-dates li{display:flex;align-items:center;height:22px}
.course-dates li::before{content:"";width:5px;height:5px;border-radius:50%;background:var(--cyan);margin-right:10px}
.course-dates .date{width:170px;white-space:nowrap}
.course-dates .rule{width:66px;height:1px;background:var(--white);margin:0 10px}
.course-dates .city{color:var(--cyan)}
</style>
</head>
<body>
<main class="brochure">
  <svg class="backdrop" viewBox="0 0 1160 826" width="1160" height="826" aria-hidden="false">
    <defs>
      <linearGradient id="skyTint" x1="0" y1="0" x2="0" y2="1">
        <stop offset="0" stop-color="#62d8f3"/>
        <stop offset="1" stop-color="#36c2e6"/>
      </linearGradient>
      <linearGradient id="greenField" x1="0" y1="0" x2="1" y2="1">
        <stop offset="0" stop-color="#3a8c1a"/>
        <stop offset="1" stop-color="#276a0e"/>
      </linearGradient>
      <linearGradient id="heliPhoto" x1="0" y1="0" x2="1" y2="1">
        <stop offset="0" stop-color="#2fb5dc"/>
        <stop offset=".6" stop-color="#6ed6f0"/>
        <stop offset="1" stop-color="#bfeefa"/>
      </linearGradient>
      <radialGradient id="jetPhoto" cx=".5" cy=".5" r=".5">
        <stop offset="0" stop-color="#c9d0d6"/>
        <stop offset="1" stop-color="#c9d0d6" stop-opacity="0"/>
      </radialGradient>
    </defs>
    <!-- left panel -->
    <rect x="0" y="0" width="577" height="420" fill="url(#skyTint)"/>
    <path d="M0,300 C90,270 200,300 300,330 C420,365 520,360 577,345 L577,826 L0,826 Z" fill="url(#greenField)" role="img" aria-label="Flag motif over green field"/>
    <rect x="0" y="583" width="580" height="66" fill="var(--white)"/>
    <rect x="260" y="523" width="312" height="178" fill="url(#jetPhoto)" role="img" aria-label="Photo of a fighter jet in flight"/>
    <!-- right panel -->
    <path d="M577,0 L1160,0 L1160,265 C960,330 760,300 577,318 Z" fill="url(#heliPhoto)" role="img" aria-label="Photo of a helicopter landing on a ship deck"/>
    <path d="M577,318 C760,300 960,330 1160,265 L1160,290 C960,350 760,325 577,345 Z" fill="var(--white)"/>
    <path d="M577,345 C760,325 960,350 1160,290 L1160,826 L1045,826 C1075,610 950,440 720,395 C660,383 615,378 577,380 Z" fill="url(#greenField)"/>
  </svg>

  <section class="panel-left">
    <div class="tab tab--light" style="top:33px">Workbook</div>
    <p class="copy copy--dark" style="top:60px">Attendees from the same company booked and paid for at the same time for the same course will received the below discounts:</p>
    <ul class="discounts" style="top:113px">
      <li>5 attendees 50% discount on the 6th attendee.</li>
      <li>10 attendees 11th attendee free</li>
      <li>&lt; 10 attendees</li>
    </ul>
    <div class="brand-seal"><span class="brand-name">Northgate<br>Trade<br>Compliance</span></div>

    <div class="tab tab--cyan" style="top:327px">Policies Cancellation</div>
    <p class="copy copy--light" style="top:364px">Cancellations incur a 20% administration fee. No cancellations permitted within 30 days of training commencing. If a registered attendee is unable to attend, a replacement attendee is allowed.</p>

    <div class="tab tab--cyan" style="top:434px">Workbook</div>
    <p class="copy copy--light" style="top:474px">Each attendees will receive a workbook. The workbook is licenced for the use of the training attendee only. If you need other copies , please order them directly.</p>

    <div class="tab tab--cyan" style="top:556px">Venue</div>
    <ul class="venues">
      <li>Harbourview Grand Hotel<br>Quay Street, Sydney</li>
      <li>Riverside Towers<br>Bank St, Melbourne</li>
    </ul>

    <div class="contact">
      <h3>CONTACT US</h3>
      <p>Email: registrations to info@northgatetc.com<br>Fax: to +61 (0)7 5000 1234</p>
    </div>
  </section>

  <section class="panel-right">
    <div class="brand-lockup">
      <span class="brand-dot"></span>
      <span class="brand-name">Northgate<br>Trade Compliance</span>
    </div>
    <h1 class="course-title">ADVANCED DEFENCE</h1>
    <div class="course-subtitle">EAR &amp; ITAR TRAINING</div>
    <div class="course-dates">
      <h2>3-DAY COURSE</h2>
      <ul>
        <li><span class="date">9, 10, 11 SEPTEMBER</span><span class="rule"></span><span class="city">MELBOURNE</span></li>
        <li><span class="date">21, 22, 23 SEPTEMBER</span><span class="rule"></span><span class="city">SYDNEY</span></li>
      </ul>
    </div>
  </section>
</main>
</body>
</html>
```